"You CAN Relax on Your Own Savings!" book cover for 80 page or so book.

Need a book cover that stands out on Bookvale, so highly engaging colors, need to reflect optimism, hope and determination. Go to Bookvale, type my name in and see the covers for the three other books I had written.

There's a lot of negativity and fear for Americans looking at retirement. Yet, they don't need that fear, my book tells them why they can be confident in their ability to retire.

There will be NO spine writing for the book, too small.

Target Market(s)

stressed out people in their 50s and 60s. This book appeals to working people, not high end, wealthy types.

Industry/Entity Type

Financial Planning

Colors

Designer to choose colors to be used in the design.

Requirements
Must have
• Needs to reflect simplicity in action.
• Please spell out my full name, GREG MALTHORPE, at the bottom of the cover.
Nice to have
• if there is anyway to put a picture of an RV (Recreational Vehicle) that would be great.
Should not have
• Do NOT want to be the stodgy, typical financial planning literature out there. No guy in a suit and tie. No one sitting on a beach.
• Do not want my face on the cover either. (On the back yes.)

```html
<!DOCTYPE html>
<html lang="en">
<head>
<meta charset="utf-8">
<title>You CAN Relax on Your Own Savings! – Book Cover</title>
<link rel="stylesheet" href="https://fonts.googleapis.com/css2?family=Russo+One&display=swap">
<style>
  :root {
    --backdrop: #f3f1ec;
    --title-blue: #1b4e9e;
    --sky-top: #8fc2e0;
    --sky-low: #c9e0ec;
    --sky-haze: #e6ecf0;
    --rock-light: #b86a4e;
    --rock: #a24f36;
    --rock-dark: #7a3826;
    --brush: #c8c4a0;
    --road: #c3c7c9;
    --author-band: rgba(228, 234, 240, 0.82);
  }
  * { margin: 0; padding: 0; box-sizing: border-box; }
  html, body {
    width: 1200px;
    height: 857px;
    overflow: hidden;
    background: var(--backdrop);
  }
  .stage {
    width: 1200px;
    height: 857px;
    display: flex;
    align-items: center;
    justify-content: center;
  }
  .book-cover {
    position: relative;
    width: 540px;
    height: 810px;
    overflow: hidden;
    box-shadow: 0 6px 18px rgba(0, 0, 0, 0.18);
    background: linear-gradient(180deg, var(--sky-top) 0%, var(--sky-low) 38%, var(--sky-haze) 48%);
  }
  .cover-sheen {
    position: absolute;
    inset: 0;
    background: linear-gradient(105deg, rgba(255,255,255,0) 50%, rgba(242,245,247,0.7) 100%);
    pointer-events: none;
    z-index: 2;
  }
  .cover-photo {
    position: absolute;
    left: 0;
    right: 0;
    top: 330px;
    bottom: 0;
    background:
      linear-gradient(90deg, rgba(0,0,0,0) 55%, rgba(233,238,241,0.55) 100%),
      linear-gradient(180deg,
        var(--rock-light) 0%,
        var(--rock) 22%,
        var(--rock-dark) 45%,
        var(--rock) 62%,
        var(--brush) 78%,
        var(--road) 100%);
    z-index: 1;
  }
  .cover-title {
    position: absolute;
    top: 62px;
    left: 0;
    right: 0;
    text-align: center;
    font-family: "Russo One", sans-serif;
    font-weight: 400;
    color: var(--title-blue);
    text-transform: uppercase;
    line-height: 1.08;
    z-index: 3;
  }
  .title-lead {
    display: block;
    font-size: 72px;
    letter-spacing: 4px;
    padding-left: 70px;
  }
  .title-middle {
    display: block;
    font-size: 38px;
    letter-spacing: 7px;
    margin-top: 4px;
    padding-left: 20px;
  }
  .title-close {
    display: block;
    font-size: 38px;
    letter-spacing: 3px;
    margin-top: 4px;
  }
  .author-band {
    position: absolute;
    left: 0;
    right: 0;
    bottom: 30px;
    height: 62px;
    background: var(--author-band);
    display: flex;
    align-items: center;
    justify-content: center;
    z-index: 3;
  }
  .author-name {
    font-family: "Russo One", sans-serif;
    font-size: 34px;
    letter-spacing: 6px;
    color: var(--title-blue);
  }
</style>
</head>
<body>
  <main class="stage">
    <section class="book-cover">
      <div class="cover-photo" role="img" aria-label="Photo of a yellow camper van (RV) driving down a desert road past tall red sandstone rock formations, with sage brush along the roadside"></div>
      <div class="cover-sheen"></div>
      <h1 class="cover-title">
        <span class="title-lead">You Can</span>
        <span class="title-middle">Relax on</span>
        <span class="title-close">Your Own Savings!</span>
      </h1>
      <div class="author-band">
        <p class="author-name">GREG MALTHORPE</p>
      </div>
    </section>
  </main>
</body>
</html>
```